Harborline Stay Collective Business Card Design

Design a business card for Harborline Stay Collective. Look at the website for colors and reference. Card should have logo, name, title, office number, mobile number, email, URL and a tagline like, "Luxury Hotel & Resort Email Marketing" (This might change).

https://www.harborlinestaycollective.net

The rest I will leave up to your imagination.

Contact Information for Business Card

Logo, name, title, office number, mobile number, email, URL and a tagline like, "Luxury Hotel & Resort Email Marketing" (This might change).

```html
<!DOCTYPE html>
<html lang="en">
<head>
<meta charset="UTF-8">
<title>Harborline Stay Collective — Business Card</title>
<link href="https://fonts.googleapis.com/css2?family=Montserrat:wght@400;500;700;800&display=swap" rel="stylesheet">
<style>
  :root {
    --stage: #2b2b2b;
    --card: #1c1c1c;
    --accent: #f07a12;
    --ink: #ffffff;
    --ink-soft: #e6e6e6;
  }
  * { box-sizing: border-box; margin: 0; padding: 0; }
  html, body {
    width: 1200px; height: 900px; overflow: hidden;
    background: var(--stage);
    font-family: "Montserrat", sans-serif;
  }
  .card {
    position: absolute;
    width: 700px; height: 400px;
    background: var(--card);
    border-bottom: 5px solid var(--accent);
    border-left: 3px solid var(--accent);
    box-shadow: 0 18px 40px rgba(0,0,0,0.55);
  }
  .card--front { left: 110px; top: 30px; }
  .card--back  { left: 390px; top: 470px; }

  /* Front */
  .front-brand {
    position: absolute; left: 0; right: 0; top: 140px;
    text-align: center;
  }
  .brand-name {
    display: inline-flex; align-items: center; gap: 14px;
    color: var(--ink);
    font-weight: 800; text-transform: uppercase;
    letter-spacing: 1px;
  }
  .brand-square {
    width: 18px; height: 18px; background: var(--accent); flex: none;
  }
  .front-brand .brand-name { font-size: 34px; }
  .tagline {
    position: absolute; left: 0; right: 0; top: 300px;
    text-align: center;
    color: var(--accent);
    font-size: 18px; font-weight: 500; letter-spacing: 0.5px;
  }

  /* Back */
  .back-brand {
    position: absolute; left: 95px; top: 200px;
    transform: translate(-50%, -50%) rotate(-90deg);
    white-space: nowrap;
  }
  .back-brand .brand-name { font-size: 19px; gap: 10px; }
  .back-brand .brand-square { width: 12px; height: 12px; }
  .divider {
    position: absolute; left: 170px; top: 40px;
    width: 1px; height: 320px; background: var(--accent);
  }
  .contact {
    position: absolute; left: 215px; top: 52px;
    color: var(--ink-soft);
  }
  .person-name {
    color: var(--accent);
    font-size: 34px; font-weight: 800; text-transform: uppercase;
    letter-spacing: 1px; line-height: 1;
  }
  .person-title { font-size: 16px; margin-top: 6px; }
  .address { font-size: 16px; line-height: 1.4; margin-top: 26px; }
  .contact-list { list-style: none; margin-top: 24px; }
  .contact-list li {
    display: flex; align-items: center; gap: 12px;
    font-size: 16px; line-height: 1.9;
  }
  .contact-list svg { width: 14px; height: 14px; fill: var(--accent); flex: none; }
</style>
</head>
<body>

<section class="card card--front" aria-label="Card front">
  <div class="front-brand">
    <span class="brand-name"><span class="brand-square"></span>Harborline Stay Collective</span>
  </div>
  <p class="tagline">Luxury Hotel &amp; Resort Email Marketing</p>
</section>

<section class="card card--back" aria-label="Card back">
  <div class="back-brand">
    <span class="brand-name"><span class="brand-square"></span>Harborline Stay Collective</span>
  </div>
  <div class="divider"></div>
  <div class="contact">
    <h1 class="person-name">Marcus Ellery</h1>
    <p class="person-title">CEO/Founder</p>
    <p class="address">Po Box, 480 B Harbor Rd<br>Bayview Point, CA 90412</p>
    <ul class="contact-list">
      <li>
        <svg viewBox="0 0 14 14" aria-hidden="true"><path d="M4 0h6a1 1 0 0 1 1 1v12a1 1 0 0 1-1 1H4a1 1 0 0 1-1-1V1a1 1 0 0 1 1-1zm0 2v9h6V2zm3 10a.7.7 0 1 0 0 1.4A.7.7 0 0 0 7 12z"/></svg>
        555.214.7300
      </li>
      <li>
        <svg viewBox="0 0 14 14" aria-hidden="true"><path d="M1 5c0-2 2.5-3 6-3s6 1 6 3v1h-3V5H4v1H1zm2 2h8l2 6H1zm4 1.5a2 2 0 1 0 0 4 2 2 0 0 0 0-4z"/></svg>
        +34 600 482 917
      </li>
      <li>
        <svg viewBox="0 0 14 14" aria-hidden="true"><path d="M0 3h14v8H0zm1.2 1L7 8l5.8-4z"/></svg>
        info@harborlinestaycollective.net
      </li>
      <li>
        <svg viewBox="0 0 14 14" aria-hidden="true"><path d="M7 0a7 7 0 1 0 0 14A7 7 0 0 0 7 0zm0 1.3c.8 0 1.7 1.6 2 4.2H5c.3-2.6 1.2-4.2 2-4.2zM1.4 5.5A5.7 5.7 0 0 1 4.3 2 11 11 0 0 0 3.7 5.5zm0 3h2.3a11 11 0 0 0 .6 3.5 5.7 5.7 0 0 1-2.9-3.5zM5 8.5h4c-.3 2.6-1.2 4.2-2 4.2s-1.7-1.6-2-4.2zm5.3 0h2.3a5.7 5.7 0 0 1-2.9 3.5 11 11 0 0 0 .6-3.5zm0-3A11 11 0 0 0 9.7 2a5.7 5.7 0 0 1 2.9 3.5z"/></svg>
        www.harborlinestaycollective.net
      </li>
    </ul>
  </div>
</section>

</body>
</html>
```